Holvern Incorporated

Holvern is a business that provides consulting, and manages and supplies trades persons in the construction and heavy industries sector. We build, do maintenance, install machinery, and can manage projects or jobs. Would like or prefer more clean, classic designs. Blacks/greys, but open to almost anything.

Target Market(s)

Industrial/Construction/Manufacturing

Industry/Entity Type

Construction Company

Contact Information for Business Card

Clean, business name on the front, possibly have the details on the back, but open to any ideas.

Logo Text

We currently do not have a slogan, open to ideas

Font styles to use
Serif
Sans Serif

Colors

Designer to choose colors to be used in the design.

Requirements
Should not have
• the oval is not my logo, was just an idea. please don't send 20 designs with the oval

```html
<!DOCTYPE html>
<html lang="en">
<head>
<meta charset="UTF-8">
<title>Holvern Incorporated — Business Card</title>
<link rel="stylesheet" href="https://fonts.googleapis.com/css2?family=Arimo:wght@400;700&family=Bitter:wght@500&display=swap">
<style>
  :root {
    --stone: #d9dbda;
    --ink: #070a0b;
    --paper: #e8e9e9;
  }
  * { margin: 0; padding: 0; box-sizing: border-box; }
  html, body {
    width: 1200px;
    height: 685px;
    overflow: hidden;
    background: var(--stone);
  }
  .card {
    position: relative;
    width: 1200px;
    height: 685px;
    overflow: hidden;
    font-family: "Arimo", Arial, sans-serif;
  }
  .card__front {
    position: absolute;
    left: 0; top: 0;
    width: 589px; height: 685px;
    background: var(--stone);
  }
  .card__back {
    position: absolute;
    left: 589px; top: 0;
    width: 611px; height: 685px;
    background: var(--ink);
  }
  .brand-name {
    position: absolute;
    left: 0; width: 589px;
    top: 300px;
    text-align: center;
    font-family: "Bitter", Georgia, serif;
    font-weight: 500;
    font-size: 64px;
    line-height: 1;
    color: var(--ink);
    letter-spacing: 1px;
  }
  .divider-mark {
    position: absolute;
    left: 548px; top: 308px;
    width: 84px; height: 72px;
  }
  .headline {
    position: absolute;
    right: 67px; top: 160px;
    text-align: right;
    color: var(--paper);
  }
  .headline__title {
    font-weight: 700;
    font-size: 50px;
    line-height: 1;
    letter-spacing: 0.5px;
  }
  .headline__sub {
    display: flex;
    align-items: center;
    justify-content: flex-end;
    gap: 10px;
    margin-top: 2px;
    font-size: 16px;
    line-height: 1;
  }
  .headline__rule {
    width: 168px;
    height: 1px;
    background: var(--paper);
  }
  .contact-list {
    position: absolute;
    left: 756px; top: 513px;
    list-style: none;
    color: var(--paper);
    font-size: 21px;
  }
  .contact-list__item {
    display: flex;
    align-items: center;
    height: 28.3px;
  }
  .contact-list__icon {
    width: 24px; height: 24px;
    margin-right: 28px;
    flex: none;
  }
</style>
</head>
<body>
<main class="card">
  <section class="card__front">
    <div class="brand-name">Holvern</div>
  </section>

  <section class="card__back">
  </section>

  <svg class="divider-mark" viewBox="0 0 84 72" aria-hidden="true">
    <polygon points="41,0 41,72 0,72" fill="#070a0b"/>
    <polygon points="41,0 84,72 41,72" fill="#d9dbda"/>
  </svg>

  <header class="headline">
    <div class="headline__title">LOREM IPSUM</div>
    <div class="headline__sub"><span class="headline__rule"></span><span>LOREM IPSUM</span></div>
  </header>

  <ul class="contact-list">
    <li class="contact-list__item">
      <svg class="contact-list__icon" viewBox="0 0 24 24" aria-hidden="true">
        <path fill="#e8e9e9" d="M6.6 10.8c1.4 2.8 3.8 5.1 6.6 6.6l2.2-2.2c.3-.3.7-.4 1-.2 1.1.4 2.3.6 3.6.6.6 0 1 .4 1 1V20c0 .6-.4 1-1 1C10.6 21 3 13.4 3 4c0-.6.4-1 1-1h3.5c.6 0 1 .4 1 1 0 1.3.2 2.5.6 3.6.1.3 0 .7-.2 1z"/>
      </svg>
      <span>(+1555-0134782</span>
    </li>
    <li class="contact-list__item">
      <svg class="contact-list__icon" viewBox="0 0 24 24" aria-hidden="true">
        <rect x="2" y="5" width="20" height="14" fill="none" stroke="#e8e9e9" stroke-width="1.8"/>
        <path d="M2 5l10 8 10-8M2 19l7.5-7M22 19l-7.5-7" fill="none" stroke="#e8e9e9" stroke-width="1.6"/>
      </svg>
      <span>simply dummy text@mailbox.com</span>
    </li>
    <li class="contact-list__item">
      <svg class="contact-list__icon" viewBox="0 0 24 24" aria-hidden="true">
        <g fill="none" stroke="#e8e9e9" stroke-width="1.6">
          <circle cx="12" cy="12" r="10"/>
          <ellipse cx="12" cy="12" rx="4.5" ry="10"/>
          <path d="M2 12h20M3.5 7h17M3.5 17h17"/>
        </g>
      </svg>
      <span>simply dummy text.com</span>
    </li>
    <li class="contact-list__item">
      <svg class="contact-list__icon" viewBox="0 0 24 24" aria-hidden="true">
        <path fill="#e8e9e9" d="M12 2C8.1 2 5 5.1 5 9c0 5.2 7 13 7 13s7-7.8 7-13c0-3.9-3.1-7-7-7zm0 9.5a2.5 2.5 0 1 1 0-5 2.5 2.5 0 0 1 0 5z"/>
      </svg>
      <span>simply dummy text</span>
    </li>
  </ul>
</main>
</body>
</html>
```